Building Servicess

We need a new business card design for a company. We specialise in: Electrical/Site temporary electrics, Data/Network Installation, Passive Fire Protection

Industry/Entity Type

Construction

Contact Information for Business Card

Services provided as detailed on project description

Font styles to use
Serif

Colors
0054AA
0677BA
7BADD7
CADEEF
E8F1F8
00AB8E
00BBA5
67D7C9
C6EFE9
E9F9F6
EB3D1F
EC4F4E
F09395
F8D3D4
FCEDEE

Requirements
Must have
• Company logo-contact details-phone numbers

```html
<!DOCTYPE html>
<html lang="en">
<head>
<meta charset="utf-8">
<title>Norvale Site Services – Business Card</title>
<link href="https://fonts.googleapis.com/css2?family=Roboto+Condensed:wght@400;700&display=swap" rel="stylesheet">
<style>
  :root {
    --canvas-bg: #eef0f2;
    --card-white: #ffffff;
    --wash-grey: #ececee;
    --brand-blue: #2f56a8;
    --brand-blue-soft: #3d64b2;
    --text-blue: #2f56a8;
    --text-grey: #55585c;
    --rule-grey: #8a8d91;
    --white: #ffffff;
  }
  * { margin: 0; padding: 0; box-sizing: border-box; }
  html, body {
    width: 1200px; height: 1000px; overflow: hidden;
    background: var(--canvas-bg);
    font-family: "Roboto Condensed", "Arial Narrow", sans-serif;
  }
  .stage {
    position: relative; width: 1200px; height: 1000px;
    display: flex; align-items: center; justify-content: center; gap: 60px;
  }
  .card {
    position: relative; width: 500px; height: 290px; overflow: hidden;
    box-shadow: 0 10px 30px rgba(0,0,0,0.12);
  }
  .card-wash { position: absolute; inset: 0; }

  /* Front */
  .card-front { background: var(--card-white); }
  .card-front .card-wash {
    background: linear-gradient(100deg, var(--wash-grey) 0%, var(--card-white) 55%);
  }
  .front-brand {
    position: absolute; top: 42px; right: 32px;
    font-weight: 700; font-size: 17px; letter-spacing: 0.5px;
    color: var(--text-blue); text-transform: uppercase;
  }
  .holder { position: absolute; left: 36px; top: 160px; }
  .holder-name { font-weight: 700; font-size: 21px; color: var(--text-blue); }
  .holder-title { font-size: 13px; color: var(--text-grey); margin-top: 2px; }
  .holder-rule { width: 250px; height: 1px; background: var(--rule-grey); margin: 8px 0 10px; }
  .contact-list { list-style: none; }
  .contact-list li {
    display: flex; align-items: center; gap: 8px;
    font-size: 13px; color: var(--text-grey); line-height: 21px;
  }
  .contact-list svg { width: 11px; height: 11px; fill: var(--text-blue); }

  /* Back */
  .card-back { background: var(--brand-blue); color: var(--white); text-align: center; }
  .card-back .card-wash {
    background: radial-gradient(ellipse at center, var(--brand-blue-soft) 0%, var(--brand-blue) 75%);
  }
  .back-content {
    position: absolute; inset: 0;
    display: flex; flex-direction: column; align-items: center; justify-content: center;
  }
  .back-brand { font-weight: 700; font-size: 24px; letter-spacing: 0.5px; text-transform: uppercase; }
  .back-rule { width: 220px; height: 1px; background: var(--white); margin: 8px 0 20px; }
  .services { font-size: 12.5px; letter-spacing: 0.4px; text-transform: uppercase; line-height: 22px; }
</style>
</head>
<body>
<main class="stage">

  <section class="card card-front" aria-label="Business card front">
    <div class="card-wash" role="img" aria-label="Light grey decorative background pattern"></div>
    <div class="front-brand">Norvale Site Services Ltd</div>
    <div class="holder">
      <div class="holder-name">Daniel Marsh</div>
      <div class="holder-title">Managing Director</div>
      <div class="holder-rule"></div>
      <ul class="contact-list">
        <li><svg viewBox="0 0 24 24" aria-hidden="true"><path d="M6.6 10.8a15.1 15.1 0 0 0 6.6 6.6l2.2-2.2a1 1 0 0 1 1-.25 11.4 11.4 0 0 0 3.6.57 1 1 0 0 1 1 1V20a1 1 0 0 1-1 1A17 17 0 0 1 3 4a1 1 0 0 1 1-1h3.5a1 1 0 0 1 1 1c0 1.25.2 2.45.57 3.6a1 1 0 0 1-.25 1z"/></svg>020 7946 0183</li>
        <li><svg viewBox="0 0 24 24" aria-hidden="true"><path d="M7 1h10a2 2 0 0 1 2 2v18a2 2 0 0 1-2 2H7a2 2 0 0 1-2-2V3a2 2 0 0 1 2-2zm0 3v14h10V4zm5 15.5a1 1 0 1 0 0 2 1 1 0 0 0 0-2z"/></svg>07700900456</li>
        <li><svg viewBox="0 0 24 24" aria-hidden="true"><circle cx="12" cy="12" r="9" fill="none" stroke="var(--text-blue)" stroke-width="2.2"/><path d="M3 12h18M12 3c3 3 3 15 0 18M12 3c-3 3-3 15 0 18" fill="none" stroke="var(--text-blue)" stroke-width="2"/></svg>norvalesite.co.uk</li>
      </ul>
    </div>
  </section>

  <section class="card card-back" aria-label="Business card back">
    <div class="card-wash" role="img" aria-label="Blue decorative background pattern"></div>
    <div class="back-content">
      <div class="back-brand">Norvale Site Services Ltd</div>
      <div class="back-rule"></div>
      <p class="services">Electrical/Site Temporary Electrics<br>Data/Network Installation &nbsp;•&nbsp; Passive Fire Protection</p>
    </div>
  </section>

</main>
</body>
</html>
```